Brochure Design Project

hi
Im looking for a great little design for my brochures. I have a home beauty salon and need a brochure menu. The name of the business is Kanade SoftGlow which is a japanese name. I'm not japanese but want it to have a slight feel of japanese, perhaps some watercolour or a traditional pattern.
Salon menu will have waxing, Facials, massage etc and would like a tri fold brochure
No bright colours please or butterflies. I want it to look and feel relaxing and peaceful. Help with a nice Logo would also be great
thanks for your help
Updates

Project Deadline Extended
Reason: I know a lot of you are busy but by extending the timeframe I can hopefully get all your creative minds flowing

hi

Just thought I'd add that I would like the brochures to be modern and edgy looking
thanks so far

Target Market(s)

People that want to be pampered and look and feel great and have a sort of natural feel ( if that makes sense)

Industry/Entity Type

Beauty Salon

Requirements
Must have
• I would like it to be A4 size and folded as a tri brochure,
Nice to have
• A classy font
Should not have
• Butterflies, swirls, bright colours or purple

```html
<!DOCTYPE html>
<html lang="en">
<head>
<meta charset="utf-8">
<title>Kanade SoftGlow – Treatment Menu</title>
<link rel="stylesheet" href="https://fonts.googleapis.com/css2?family=Didact+Gothic&family=Questrial&display=swap">
<style>
  :root {
    --page-bg: #e9e6e3;
    --sky: #a8c6ec;
    --mist: #cdd2ec;
    --blush: #f3c8db;
    --ink: #58585c;
    --accent-pink: #e0569a;
    --accent-blue: #6f9fd6;
    --band-blue: #8fb4e3;
    --band-pink: #efb9d3;
    --paper: #ffffff;
    --leader: #8c8c92;
    --fold: rgba(255,255,255,0.55);
  }
  * { box-sizing: border-box; margin: 0; padding: 0; }
  html, body {
    width: 1200px; height: 937px; overflow: hidden;
    background: var(--page-bg);
    font-family: "Didact Gothic", "Questrial", sans-serif;
    color: var(--ink);
  }
  .brochure {
    position: absolute; left: 20px; top: 58px;
    width: 1160px; height: 820px;
    background: linear-gradient(180deg, var(--sky) 0%, var(--mist) 45%, var(--blush) 100%);
    box-shadow: 0 6px 18px rgba(0,0,0,0.25);
    overflow: hidden;
  }
  .fold { position: absolute; top: 0; bottom: 0; width: 1px; background: var(--fold); }
  .fold--one { left: 387px; }
  .fold--two { left: 773px; }

  .backdrop-circles { position: absolute; left: 0; top: 0; }

  .blossom-branch {
    position: absolute;
    background: radial-gradient(ellipse at 40% 50%, rgba(250,214,230,0.95) 0%, rgba(244,190,214,0.7) 45%, rgba(244,190,214,0) 75%);
  }
  .blossom-branch--top { left: 0; top: 0; width: 370px; height: 130px; }
  .blossom-branch--bottom { left: 740px; top: 630px; width: 420px; height: 190px; }

  .photo { position: absolute; }
  .photo--facial {
    left: 0; top: 583px; width: 348px; height: 237px;
    background: linear-gradient(135deg, #c9b7a8 0%, #efe1d8 45%, #f6eef0 100%);
  }
  .photo-band--pink { position: absolute; left: 0; top: 565px; width: 348px; height: 18px; background: var(--band-pink); }
  .photo--stones {
    left: 813px; top: 0; width: 347px; height: 282px;
    background: linear-gradient(160deg, #f4f1ee 0%, #d9b09b 45%, #b57f66 75%, #efe9e6 100%);
  }
  .photo-band--blue { position: absolute; left: 813px; top: 282px; width: 347px; height: 20px; background: var(--band-blue); }

  .section-label {
    position: absolute;
    background: var(--paper);
    font-family: "Questrial", sans-serif;
    font-weight: 400;
    font-size: 22px; letter-spacing: 1px;
    padding: 2px 8px 0;
    height: 31px; line-height: 29px;
  }
  .section-label--facials { left: 40px; top: 131px; color: var(--accent-pink); }
  .section-label--massage { left: 812px; top: 327px; color: var(--accent-blue); }

  .treatment { position: absolute; width: 309px; }
  .price-row { display: flex; align-items: baseline; white-space: nowrap; }
  .price-row .leader { flex: 1; border-bottom: 1px solid var(--leader); margin: 0 2px; transform: translateY(-3px); }
  .price-row--main { font-size: 18px; line-height: 23px; }
  .price-row--series { font-size: 15px; line-height: 21px; }
  .treatment-desc {
    font-size: 14.6px; line-height: 19px;
    text-align: justify; hyphens: none;
  }
  .allow { font-style: italic; }

  .treatment--express { left: 40px; top: 190px; }
  .treatment--signature { left: 40px; top: 357px; }
  .treatment--vitamin { left: 427px; top: 80px; }
  .treatment--mens { left: 427px; top: 545px; }
  .treatment--bare-back { left: 427px; top: 682px; }
  .treatment--hot-stone { left: 813px; top: 387px; }
  .treatment--body { left: 813px; top: 490px; }
  .treatment--back { left: 813px; top: 612px; }

  .feature-box {
    position: absolute; left: 427px; top: 356px;
    width: 308px; height: 154px;
    background: var(--paper);
    padding: 9px 10px 0 11px;
  }
  .feature-box .price-row--main { color: var(--accent-pink); font-size: 17px; }
</style>
</head>
<body>
  <article class="brochure" aria-label="Kanade SoftGlow treatment menu, tri-fold inside">
    <svg class="backdrop-circles" width="1160" height="820" aria-hidden="true">
      <circle cx="158" cy="720" r="70" fill="#ffffff" opacity="0.18"/>
      <circle cx="545" cy="650" r="75" fill="#ecb8d2" opacity="0.35"/>
      <circle cx="655" cy="720" r="75" fill="#b9bfe8" opacity="0.35"/>
      <circle cx="1060" cy="610" r="70" fill="#ffffff" opacity="0.12"/>
    </svg>

    <div class="fold fold--one"></div>
    <div class="fold fold--two"></div>

    <!-- Left panel -->
    <div class="blossom-branch blossom-branch--top" role="img" aria-label="Pink cherry blossom branch"></div>
    <h2 class="section-label section-label--facials">FACIALS</h2>

    <section class="treatment treatment--express">
      <div class="price-row price-row--main"><span>Express Glow Facial</span><span class="leader"></span><span>$40.00</span></div>
      <div class="price-row price-row--series"><span>Series of 3</span><span class="leader"></span><span>$105.00</span></div>
      <p class="treatment-desc">When time is of the essence, this Express Facial treatment will revitalise your skin’s radiance, leaving it with a healthy glow. Includes cleansing, exfoliation, pressure point massage, moisturiser and sunscreen. <span class="allow">Allow 30 min</span></p>
    </section>

    <section class="treatment treatment--signature">
      <div class="price-row price-row--main"><span>Kanade Signature Facial</span><span class="leader"></span><span>$75.00</span></div>
      <div class="price-row price-row--series"><span>Series of 3</span><span class="leader"></span><span>$200.00</span></div>
      <p class="treatment-desc">Enjoy an hour of total relaxation and emerge looking and feeling great! This facial is the ultimate for the over worked and over stressed. Your customised facial will begin with a deep cleanse, followed by a gentle exfoliation, mask, massage and completed with a nourishing moisturizer and eye crème. <span class="allow">Allow 1 hr</span></p>
    </section>

    <div class="photo-band--pink"></div>
    <div class="photo photo--facial" role="img" aria-label="Photo of a relaxing facial massage with flowers"></div>

    <!-- Center panel -->
    <section class="treatment treatment--vitamin">
      <div class="price-row price-row--main"><span>Vitamin C facial</span><span class="leader"></span><span>$70.00</span></div>
      <div class="price-row price-row--main"><span>Brightening treatment</span></div>
      <div class="price-row price-row--series"><span>Series of 3</span><span class="leader"></span><span>$190.00</span></div>
      <p class="treatment-desc">This facial treatment uses a concentrated complex of topical vitamin C that is easily absorbed by the skin. This helps battle the visible signs of ageing. This formulation has been proven in the medical field to be an antioxidant that works by mopping up damaging chemical compounds known as “free radicals.” This topical antioxidant also stimulates the production of collagen. <span class="allow">Allow 1hr</span></p>
    </section>

    <section class="feature-box">
      <div class="price-row price-row--main"><span>Kanade Ultimate Tranquility ....$95.00</span></div>
      <p class="treatment-desc">This blissful treatment starts with a dry body brush, jojoba oil is then drizzled over the back, followed by a completely relaxing hot stone back massage. To finish off, your skin is treated to a indulgently nourishing facial. <span class="allow">Allow 1 hr 15min</span></p>
    </section>

    <section class="treatment treatment--mens">
      <div class="price-row price-row--main"><span>Kanade Man</span><span class="leader"></span><span>$70.00</span></div>
      <div class="price-row price-row--series"><span>Series of 3</span><span class="leader"></span><span>$190.00</span></div>
      <p class="treatment-desc">Maintain the vitality and look of healthy skin with a double cleanse, exfoliate facial massage, and a hydrating mask.</p>
    </section>

    <section class="treatment treatment--bare-back">
      <div class="price-row price-row--main"><span>Bare Back Purification</span><span class="leader"></span><span>$50.00</span></div>
      <p class="treatment-desc">This includes a deep cleanse. Exfoliation, extractions, mask and moisturizer to leave your back feeling smooth and refreshed. <span class="allow">Allow 30min</span></p>
    </section>

    <!-- Right panel -->
    <div class="photo photo--stones" role="img" aria-label="Photo of a hot stone back massage"></div>
    <div class="photo-band--blue"></div>
    <h2 class="section-label section-label--massage">MASSAGE</h2>

    <section class="treatment treatment--hot-stone">
      <div class="price-row price-row--main"><span>Full body Hot Stone Massage</span><span class="leader"></span><span>$85.00</span></div>
      <p class="treatment-desc">This treatment melts away tension with smooth warm basalt stones and will put you in the ultimate relaxed state. <span class="allow">Allow 1hr</span></p>
    </section>

    <section class="treatment treatment--body">
      <div class="price-row price-row--main"><span>Body massage</span><span class="leader"></span><span>$60.00</span></div>
      <p class="treatment-desc">Relaxing the body as well as the mind will rejuvenate and awaken your spirit. Choose a Relaxation, Swedish or Aromatherapy massage. <span class="allow">Allow 1 hr</span></p>
    </section>

    <section class="treatment treatment--back">
      <div class="price-row price-row--main"><span>Back Massage</span><span class="leader"></span><span>$50.00</span></div>
      <p class="treatment-desc"><span class="allow">Allow 1/2 hr</span></p>
    </section>

    <div class="blossom-branch blossom-branch--bottom" role="img" aria-label="Pink cherry blossom branch"></div>
  </article>
</body>
</html>
```